Ringwell Lookup - Web design / template design

Hello,

I need a design for my existing site. I already have a logo that I want to use, which you can find on my site ( I can also provide different formats / larger versions ).

Please see http://www.ringwelllookup.example for details of the site.

What I need are pages with sections that can be edited, so for example, I need basic table / div content sections that I can place in the members area that can contain whatever custom content I need to put in them without the table / div design getting stretched out or skewed.

The main page, basically needs to have all of the content on the current page or room for it at least should I want to add it.

You can also see ww2.ringwelllookup.example with more info ( not a live site and me trying my best to do something, but I'm just not good at design :)

The site content for the most part needs to be actual text, rather than text on images. I will need to change this content and have it indexed by search engines, if you want, you can just put filler text in. There are exceptions of course, like maybe on the main page, if there are boxes with some static image text, that is fine.

Target Market(s)

Telephony, phone service providers, phone system users

Industry/Entity Type

It Service

Requirements
Must have
• Dynamic content capabilities.

Logo colors implemented in the site in some way.

Easy navigation ( tabs at the top are good or whatever you think ).

I will have the following sections:

1. Home
2. About us ( company info ).
3. How to / Help
4. Pricing
5. Support section.
6. Contact section
7. Singup section
8. Members section

I would like the main page to be more image / wow factor and the other pages really just need to be basic layout and places to put tables or divs with content in them. Table or div header images are for titles are ok as long as I can edit them.

Nice to have
• Sign up button placed somewhere.

Twitter / Facebook / LinkedIn buttons

Should not have
• Flash or all page content in static images.

```html
<!DOCTYPE html>
<html lang="en">
<head>
<meta charset="utf-8">
<title>Ringwell Lookup – CNAM Provider</title>
<link rel="stylesheet" href="https://fonts.googleapis.com/css2?family=Open+Sans:wght@400;600;700&display=swap">
<style>
:root{
  --page-top:#a6abae;
  --page-mid:#e3e5e6;
  --navy:#18222e;
  --gold:#f2a71b;
  --white:#ffffff;
  --ink:#111111;
  --box-line:#b9bcbf;
  --footer:#7b8184;
  --link-blue:#1a2fd0;
  --photo-left-a:#8a8f92;
  --photo-left-b:#c9c3bb;
  --photo-right-a:#c8d4df;
  --photo-right-b:#e9d6c4;
}
*{margin:0;padding:0;box-sizing:border-box}
html,body{width:980px;height:1200px;overflow:hidden}
body{
  position:relative;
  font-family:"Open Sans",Verdana,sans-serif;
  color:var(--ink);
  background:linear-gradient(180deg,var(--page-top) 0,#c9cccd 420px,var(--page-mid) 700px,var(--page-mid) 1100px);
}
.site-header{position:absolute;left:15px;top:29px;width:948px;height:101px;background:var(--navy);border-radius:4px;overflow:hidden}
.tagline-tab{position:absolute;left:260px;top:0;width:688px;height:38px}
.tagline{position:absolute;left:338px;top:11px;font-size:12.3px;line-height:17px;color:#222;white-space:nowrap}
.brand{position:absolute;left:13px;top:30px;font-size:33px;line-height:44px;font-weight:400;color:var(--white);letter-spacing:-.3px;white-space:nowrap}
.main-nav{position:absolute;left:368px;top:60px;display:flex;font-size:12.3px;line-height:17px;color:var(--white);white-space:nowrap}
.main-nav a{color:var(--white);text-decoration:none}
.main-nav a.current{color:var(--gold)}
.main-nav .sep{margin:0 14px}
.hero{position:absolute;left:15px;top:131px;width:948px;height:342px;display:flex}
.hero-photo{height:100%}
.hero-photo.team{width:493px;background:linear-gradient(120deg,var(--photo-left-a),var(--photo-left-b) 55%,#7f8486)}
.hero-photo.support{width:455px;background:linear-gradient(90deg,#4b5a66,var(--photo-right-a) 45%,var(--photo-right-b))}
.content-sheet{position:absolute;left:15px;top:481px;width:948px;height:603px;background:var(--white);border-radius:3px}
.panel{position:absolute;background:var(--white);border:1px solid var(--box-line);border-radius:5px;box-shadow:0 1px 2px rgba(0,0,0,.12)}
.panel h2{font-size:13px;font-weight:600;position:absolute}
.panel p{font-size:12.2px;line-height:16px;margin-bottom:16px}
.questions{left:27px;top:494px;width:262px;height:129px}
.questions h2{left:28px;top:19px}
.chat-bubble{position:absolute;left:25px;top:54px}
.chat-name{position:absolute;left:45px;top:61px;font-size:12px;font-weight:700;color:var(--link-blue);white-space:nowrap}
.chat-status{position:absolute;left:45px;top:77px;font-size:11.5px}
.features{left:27px;top:635px;width:262px;height:439px}
.features h2{left:28px;top:19px}
.feature-list{position:absolute;left:17px;top:49px;list-style:none;font-size:12.2px;line-height:21px;width:244px}
.feature-list li{padding-left:11px;text-indent:-11px}
.feature-list li::before{content:"* "}
.feature-list li.wrap{line-height:17px;padding-top:2px;padding-bottom:2px}
.about{left:300px;top:494px;width:651px;height:279px}
.about h2{left:21px;top:19px}
.about .body{position:absolute;left:21px;top:54px;width:620px}
.cnam{left:300px;top:785px;width:651px;height:279px}
.cnam h2{left:16px;top:17px}
.cnam .body{position:absolute;left:16px;top:53px;width:622px}
.cnam .body p{line-height:18px;margin-bottom:18px}
.site-footer{position:absolute;left:0;top:1108px;width:980px;height:92px;background:var(--footer);color:var(--white)}
.footer-nav{position:absolute;left:333px;top:25px;font-size:12.5px;white-space:nowrap}
.footer-nav .sep{margin:0 13px}
.copyright{position:absolute;left:362px;top:60px;font-size:13px;font-weight:600;white-space:nowrap}
</style>
</head>
<body>
<header class="site-header">
  <svg class="tagline-tab" width="688" height="38" viewBox="0 0 688 38">
    <path d="M0 0 H684 Q688 0 688 4 V38 H62 Q48 38 40 24 L30 10 Q24 0 10 0 Z" fill="#ffffff"/>
  </svg>
  <p class="tagline">CNAM Provider For VoIP Based Phone Systems - Get Caller Name On Your Inbounde VoIP Calls</p>
  <div class="brand">Ringwell Lookup</div>
  <nav class="main-nav">
    <a class="current" href="#">HOME</a><span class="sep">|</span>
    <a href="#">CNAM HOW TO</a><span class="sep">|</span>
    <a href="#">LOW RATES</a><span class="sep">|</span>
    <a href="#">CONTACT US</a><span class="sep">|</span>
    <a href="#">JOIN FOR FREE</a><span class="sep">|</span>
    <a href="#">LOGIN</a>
  </nav>
</header>

<section class="hero">
  <div class="hero-photo team" role="img" aria-label="Photo of three business colleagues reviewing documents in an office"></div>
  <div class="hero-photo support" role="img" aria-label="Photo of a smiling support agent wearing a headset in a call centre"></div>
</section>

<main class="content-sheet"></main>

<aside class="panel questions">
  <h2>Have Questions?:</h2>
  <svg class="chat-bubble" width="200" height="62" viewBox="0 0 200 62">
    <path d="M4 .5 H194 Q198.5 .5 198.5 4 V45 Q198.5 49.5 194 49.5 H26 L17 58 L17 49.5 H4 Q.5 49.5 .5 45 V4 Q.5 .5 4 .5 Z" fill="#fff" stroke="#555"/>
    <circle cx="12" cy="14" r="4" fill="#f2a71b"/>
  </svg>
  <span class="chat-name">RingwellLookup.example Chat</span>
  <span class="chat-status">Away</span>
</aside>

<aside class="panel features">
  <h2>Features:</h2>
  <ul class="feature-list">
    <li>No monthly fees</li>
    <li>No account minimums</li>
    <li>5 FREE Queries to test our service</li>
    <li>United States and Canada CNAM</li>
    <li>High quality CNAM results</li>
    <li>Free configuration assistance</li>
    <li>Low per query rates ( from $0.0077 )</li>
    <li class="wrap">Automatic discounts by your query volume</li>
    <li>Automatic discounts for UNVAILABLE</li>
    <li>Instant setup and account activation</li>
    <li>NO charge for invalid lookups</li>
    <li>Easy integration with your PBX or VoIP</li>
    <li>Up to date Caller ID name records.</li>
    <li>Easy to use administration panel</li>
    <li>Simple HTTP based API</li>
    <li class="wrap">Searchable CNAM query records via your admin panel</li>
  </ul>
</aside>

<section class="panel about">
  <h2>About Us</h2>
  <div class="body">
    <p>RingwellLookup.example is a leading provider of CNAM / Caller ID Name services for VoIP providers and PBX systems. We support United States and Canadian phone numbers. Our service integrates seamlessly with all types of PBX systems including Starline, callbox, Tonalis, Dialium, Plexio, OpenBranch, LibreSwitch and more!</p>
    <p>We have access to all of the major CNAM databases in the United States and Canada, something we're proud to offer.Use our easy to use examples to begin delivering caller ID name to your PBX or VoIP customers in minutes.</p>
    <p>Our super low rates, high quality results and unprecedented features set us apart from our competitors. You'll have no monthly fees, instant setup and automatic CNAM query price reductions based on your monthly query volume, features that our competitors simply don't provide!</p>
  </div>
</section>

<section class="panel cnam">
  <h2>What is CNAM?</h2>
  <div class="body">
    <p>CNAM is a database of caller names used to identify the name of a caller when receiving an inbound call from the United States or Canada.</p>
    <p>The name of a caller is determined by searching a database for a name associated with the phone number of the calling party. You likely receive caller ID name produced by a lookup into a CNAM database on your land line phone service at home.</p>
    <p>Since the process of matching the caller's number to a CNAM database requires additional hardware and maitenence, it's likely that your VoIP provider does not provide caller ID name services with your inbound voice over IP calls, so you see only the number of the caller, preventing you from identifying the caller before you answer your calls.</p>
  </div>
</section>

<footer class="site-footer">
  <div class="footer-nav">Privacy Policy<span class="sep">|</span>Terms and conditions<span class="sep">|</span>Contact Us</div>
  <div class="copyright">Copyright 2011 RingwellLookup.example</div>
</footer>
</body>
</html>
```